Copperleaf Motorized Shade Business Card

Hello, we've had our logo made. Now we are looking for a clean and cool looking business card. One side can just be the logo with any design elements that might look good with it. The other side will be Name, Phone Number and Email. There will not be an address on the card.

```html
<!DOCTYPE html>
<html lang="en">
<head>
<meta charset="utf-8">
<title>Copperleaf Motorized Shade – Business Card</title>
<link rel="stylesheet" href="https://fonts.googleapis.com/css2?family=Oswald:wght@400;600&family=PT+Serif&display=swap">
<style>
  :root {
    --bg: #8a8a8a;
    --bg-light: #b4b4b4;
    --card: #f7f7f7;
    --card-edge: #e4e4e4;
    --navy: #1f3a78;
    --sky: #3d9fd9;
    --sun: #f5c84a;
    --divider: #cfcfcf;
  }
  * { box-sizing: border-box; margin: 0; padding: 0; }
  html, body { width: 1200px; height: 900px; overflow: hidden; }
  body {
    background: radial-gradient(ellipse at 50% 40%, var(--bg-light), var(--bg));
    display: flex;
    align-items: center;
    justify-content: center;
    gap: 40px;
    font-family: "Oswald", sans-serif;
  }
  .card {
    width: 540px;
    height: 310px;
    background: var(--card);
    border-radius: 26px;
    box-shadow: 0 2px 0 var(--card-edge), 0 18px 30px rgba(0,0,0,0.25);
    position: relative;
    display: flex;
    align-items: center;
  }
  .brand {
    display: flex;
    align-items: center;
    gap: 12px;
    color: var(--navy);
    font-weight: 600;
  }
  .brand-dot {
    width: 22px; height: 22px;
    border-radius: 50%;
    background: var(--sun);
    flex: none;
  }
  .brand-name { line-height: 1.05; text-transform: uppercase; }
  .brand-name .primary { display: block; font-size: 40px; letter-spacing: 1px; }
  .brand-name .secondary { display: block; font-size: 16px; letter-spacing: 3px; }

  .card--info .brand-panel {
    width: 50%;
    display: flex;
    justify-content: center;
  }
  .card--info .brand .primary { font-size: 30px; }
  .card--info .brand .secondary { font-size: 12px; letter-spacing: 2px; }
  .card--info .brand-dot { width: 16px; height: 16px; }
  .divider {
    width: 1px;
    height: 150px;
    background: var(--divider);
  }
  .contact-panel { padding-left: 34px; }
  .person-name {
    font-size: 30px;
    font-weight: 600;
    color: var(--navy);
    letter-spacing: 0.5px;
  }
  .job-title {
    font-size: 16px;
    font-weight: 400;
    color: var(--sky);
    letter-spacing: 1px;
    margin-bottom: 16px;
  }
  .contact-line {
    display: flex;
    align-items: center;
    gap: 10px;
    font-family: "PT Serif", serif;
    font-size: 15px;
    color: var(--navy);
    margin-top: 6px;
  }
  .contact-line svg { width: 14px; height: 14px; fill: var(--sky); flex: none; }

  .card--logo { justify-content: center; }
</style>
</head>
<body>
  <section class="card card--info">
    <div class="brand-panel">
      <div class="brand">
        <span class="brand-dot"></span>
        <span class="brand-name"><span class="primary">Copperleaf</span><span class="secondary">Motorized Shade</span></span>
      </div>
    </div>
    <div class="divider"></div>
    <div class="contact-panel">
      <h1 class="person-name">YOUR NAME</h1>
      <p class="job-title">JOB TITLE</p>
      <p class="contact-line">
        <svg viewBox="0 0 24 24" aria-hidden="true"><path d="M6.6 10.8a15.1 15.1 0 0 0 6.6 6.6l2.2-2.2a1 1 0 0 1 1-.25 11.4 11.4 0 0 0 3.6.57 1 1 0 0 1 1 1V20a1 1 0 0 1-1 1A17 17 0 0 1 3 4a1 1 0 0 1 1-1h3.5a1 1 0 0 1 1 1c0 1.25.2 2.45.57 3.57a1 1 0 0 1-.25 1z"/></svg>
        000 000 0000
      </p>
      <p class="contact-line">
        <svg viewBox="0 0 24 24" aria-hidden="true"><path d="M2 5h20v14H2z M2 5l10 8 10-8" /></svg>
        youremail@xyz.com
      </p>
    </div>
  </section>

  <section class="card card--logo">
    <div class="brand">
      <span class="brand-dot"></span>
      <span class="brand-name"><span class="primary">Copperleaf</span><span class="secondary">Motorized Shade</span></span>
    </div>
  </section>
</body>
</html>
```